Business card design for new eCommerce site focusing on integrity and strong businsess tactics

We need a business card that will stand out and be memorable. Something with color that matches our company logo colors. Think high end version of Dealvine. There are 2 logos provided. The parent company is called Bright Harbor Ventures and we are presenting a new and very exciting eCommerce site called KeenTraders.example.

Target Market(s)

Our target markets are in the Activities, Food and Beverage, Health and Beauty

Industry/Entity Type

Marketing

Contact Information for Business Card

We have 4 members that need cards...I will provide all info to the winner of the design contest
Business Address is
48730 West 61st Avenue, Suite C204
Phoenix AZ 85917

Font styles to use
Serif
Sans Serif

Colors

Designer to choose colors to be used in the design.

Requirements
Must have
• The card must be memorable...should be unique in design but must exude integrity and be playful .
• I have provided several colors or our parent company...please feel free to use which ever
Nice to have
• I will leave this up to you. Feel free to use other images of your choosing that wraps around our client.....Activities, Dining, Health, Beauty
Should not have
• just dont be boring

```html
<!DOCTYPE html>
<html lang="en">
<head>
<meta charset="utf-8">
<title>KeenTraders.example business card</title>
<link href="https://fonts.googleapis.com/css2?family=Questrial&display=swap" rel="stylesheet">
<style>
  :root {
    --green: #76b843;
    --green-light: #8cc63f;
    --blue: #2b7fb3;
    --paper: #f7f7f7;
    --paper-shade: #e6e6e6;
    --ink: #3a3a3a;
    --backdrop: #2c2c2c;
    --white: #ffffff;
  }
  html, body {
    margin: 0;
    width: 1200px;
    height: 834px;
    overflow: hidden;
    background: var(--backdrop);
    font-family: "Questrial", "Century Gothic", sans-serif;
  }
  .stage {
    position: relative;
    width: 1200px;
    height: 834px;
  }
  .card {
    position: absolute;
    top: 262px;
    width: 540px;
    height: 309px;
    background: linear-gradient(160deg, var(--white), var(--paper) 55%, var(--paper-shade));
    overflow: hidden;
    box-shadow: 0 14px 30px rgba(0,0,0,.45);
  }
  .card-front { left: 40px; }
  .card-back { left: 620px; }
  .card svg.shapes { position: absolute; inset: 0; }

  .brand {
    position: absolute;
    display: flex;
    align-items: center;
    gap: 10px;
  }
  .brand-dot {
    width: 26px;
    height: 26px;
    border-radius: 50%;
    background: var(--blue);
    flex: none;
  }
  .brand-name {
    color: var(--green);
    font-size: 30px;
    line-height: 1;
    letter-spacing: -0.5px;
  }
  .brand-tagline {
    color: var(--ink);
    font-size: 12px;
    letter-spacing: 1px;
    margin-top: 4px;
  }
  .card-front .brand { left: 42px; top: 100px; }

  .partner {
    position: absolute;
    right: 34px;
    top: 28px;
    display: flex;
    flex-direction: column;
    align-items: center;
    gap: 6px;
  }
  .partner-badge {
    width: 50px;
    height: 50px;
    border-radius: 50%;
    background: var(--green-light);
  }
  .partner-name {
    color: var(--green);
    font-size: 11px;
  }

  .card-back .brand { left: 42px; top: 112px; }
  .card-back .brand-name { font-size: 26px; }
  .card-back .brand-dot { width: 22px; height: 22px; }
  .card-back .brand-tagline { font-size: 11px; }

  .person {
    position: absolute;
    right: 34px;
    top: 26px;
    text-align: right;
  }
  .person-name {
    color: var(--white);
    font-size: 17px;
    letter-spacing: 1px;
  }
  .person-title {
    color: var(--blue);
    font-size: 14px;
    margin-top: 2px;
  }

  .contact {
    position: absolute;
    right: 26px;
    top: 118px;
    list-style: none;
    margin: 0;
    padding: 0;
    color: var(--ink);
    font-size: 11px;
    text-align: right;
  }
  .contact li {
    display: flex;
    justify-content: flex-end;
    align-items: center;
    gap: 7px;
    margin-bottom: 6px;
  }
  .contact svg { width: 11px; height: 11px; flex: none; }

  .address {
    position: absolute;
    left: 34px;
    bottom: 30px;
    color: var(--white);
    font-size: 11px;
    line-height: 1.7;
    font-style: normal;
  }
</style>
</head>
<body>
<main class="stage">

  <section class="card card-front" aria-label="Card front">
    <svg class="shapes" viewBox="0 0 540 309" preserveAspectRatio="none" aria-hidden="true">
      <path fill="var(--green)" d="M0,255 C150,300 300,298 380,215 C440,155 495,145 540,145 L540,309 L0,309 Z"/>
      <path fill="var(--blue)" d="M0,266 C150,306 305,305 388,228 C448,172 500,160 540,160 L540,309 L0,309 Z"/>
    </svg>
    <div class="brand">
      <span class="brand-dot"></span>
      <div>
        <div class="brand-name">KeenTraders.example</div>
        <div class="brand-tagline">Outings-Eateries-Wellness-Style</div>
      </div>
    </div>
    <div class="partner">
      <span class="partner-badge"></span>
      <span class="partner-name">Bright Harbor Ventures</span>
    </div>
  </section>

  <section class="card card-back" aria-label="Card back">
    <svg class="shapes" viewBox="0 0 540 309" preserveAspectRatio="none" aria-hidden="true">
      <path fill="var(--blue)" d="M215,0 C265,55 345,88 430,92 C360,72 300,40 262,0 Z"/>
      <path fill="var(--green)" d="M285,0 C330,75 450,108 540,98 L540,0 Z"/>
      <path fill="var(--blue)" d="M190,176 C280,170 360,205 400,252 C355,218 285,192 190,186 Z"/>
      <path fill="var(--green)" d="M0,212 C80,180 220,176 305,218 C345,240 365,278 372,309 L0,309 Z"/>
    </svg>
    <div class="person">
      <div class="person-name">DARA QUILL</div>
      <div class="person-title">President</div>
    </div>
    <div class="brand">
      <span class="brand-dot"></span>
      <div>
        <div class="brand-name">KeenTraders.example</div>
        <div class="brand-tagline">Outings-Eateries-Wellness-Style</div>
      </div>
    </div>
    <ul class="contact">
      <li>555-014-2290
        <svg viewBox="0 0 12 12" aria-hidden="true"><path fill="var(--blue)" d="M2.5,1 L4.5,1 L5.2,3.5 L4,4.4 C4.6,5.8 6.2,7.4 7.6,8 L8.5,6.8 L11,7.5 L11,9.5 C11,10.3 10.3,11 9.5,11 C5,11 1,7 1,2.5 C1,1.7 1.7,1 2.5,1Z"/></svg>
      </li>
      <li>dara@keentraders.example
        <svg viewBox="0 0 12 12" aria-hidden="true"><rect x="1" y="2.5" width="10" height="7" fill="none" stroke="var(--blue)" stroke-width="1.3"/><path d="M1,2.5 L6,6.5 L11,2.5" fill="none" stroke="var(--blue)" stroke-width="1.3"/></svg>
      </li>
      <li>www.keentraders.example
        <svg viewBox="0 0 12 12" aria-hidden="true"><circle cx="6" cy="6" r="5" fill="none" stroke="var(--blue)" stroke-width="1.2"/><ellipse cx="6" cy="6" rx="2.2" ry="5" fill="none" stroke="var(--blue)" stroke-width="1"/><path d="M1,6 H11" stroke="var(--blue)" stroke-width="1"/></svg>
      </li>
    </ul>
    <address class="address">
      48730 West 61st Avenue,<br>
      Suite C204 Phoenix<br>
      AZ 85917
    </address>
  </section>

</main>
</body>
</html>
```